Innovative Bitcoin Powerpoint Presentation

I have constructred most of the data for a 15 page powerpoint presentation on an innovative bitcoin idea that provides access to fiat currency with bitcoin hodlings

I need this to look great as a first blush to potential investors

Reason: updated deck and name

Target Market(s)

Venture Capital firms and private equity firms

Requirements
Must have
• Fun, innovateive deck, very clean
Should not have
• any generic feel - no templates

```html
<!DOCTYPE html>
<html lang="en">
<head>
<meta charset="utf-8">
<title>Northvale – Team</title>
<link href="https://fonts.googleapis.com/css2?family=Montserrat:wght@500;600;700&family=Roboto:wght@300;400;500&display=swap" rel="stylesheet">
<style>
  :root {
    --backdrop: #151515;
    --slide-light: #eeeff0;
    --slide-mid: #dcdddf;
    --ink: #111111;
    --body-grey: #6f6f6f;
    --role-ink: #333333;
    --orange: #f3aa4e;
    --teal: #45b69c;
    --blue: #3174b8;
    --placeholder: #c9c9c9;
  }
  html, body {
    margin: 0;
    width: 1200px;
    height: 1200px;
    overflow: hidden;
    background: var(--backdrop);
  }
  .slide {
    position: absolute;
    left: 0;
    top: 225px;
    width: 1200px;
    height: 750px;
    display: block;
  }
  .title { font-family: "Montserrat", sans-serif; font-weight: 700; font-size: 52px; fill: var(--ink); }
  .brand-name { font-family: "Montserrat", sans-serif; font-weight: 600; font-size: 40px; fill: var(--ink); }
  .brand-tagline { font-family: "Montserrat", sans-serif; font-weight: 500; font-size: 13px; letter-spacing: 1.4px; fill: var(--role-ink); }
  .member-name { font-family: "Roboto", sans-serif; font-weight: 500; font-size: 17px; }
  .member-name.orange { fill: var(--orange); }
  .member-name.teal { fill: var(--teal); }
  .member-role { font-family: "Roboto", sans-serif; font-weight: 400; font-size: 13px; fill: var(--role-ink); }
  .member-bio { font-family: "Roboto", sans-serif; font-weight: 300; font-size: 13px; fill: var(--body-grey); }
  .page-label { font-family: "Montserrat", sans-serif; font-weight: 500; font-size: 20px; fill: #ffffff; }
  .page-number { font-family: "Montserrat", sans-serif; font-weight: 700; font-size: 21px; fill: #ffffff; }
</style>
</head>
<body>
<svg class="slide" viewBox="0 0 1200 750" xmlns="http://www.w3.org/2000/svg">
  <defs>
    <linearGradient id="slide-bg" x1="0" y1="0" x2="1" y2="1">
      <stop offset="0" stop-color="#d2d3d5"/>
      <stop offset="0.45" stop-color="var(--slide-light)"/>
      <stop offset="1" stop-color="var(--slide-mid)"/>
    </linearGradient>
    <linearGradient id="header-rule" x1="0" y1="0" x2="1" y2="0">
      <stop offset="0" stop-color="#3a76b5"/>
      <stop offset="0.3" stop-color="#777777"/>
      <stop offset="0.55" stop-color="#f3aa4e"/>
      <stop offset="0.8" stop-color="#9bb86a"/>
      <stop offset="1" stop-color="#45b69c"/>
    </linearGradient>
  </defs>

  <rect class="slide-background" width="1200" height="750" fill="url(#slide-bg)" role="img" aria-label="Soft grey low-poly geometric backdrop"/>

  <rect class="header-rule" x="0" y="74" width="892" height="3" fill="url(#header-rule)"/>

  <g class="brand">
    <text class="brand-name" x="1169" y="86" text-anchor="end">Northvale</text>
    <text class="brand-tagline" x="1169" y="105" text-anchor="end">Liquidity on demand</text>
  </g>

  <text class="title" x="56" y="208">Team</text>

  <g class="member member-lead">
    <polygon points="351,191 810,191 582,407" fill="var(--orange)"/>
    <circle cx="697" cy="304" r="75" fill="var(--placeholder)" role="img" aria-label="Portrait of Marcus R. Delane"/>
    <g class="photo-icon" transform="translate(677,286)" fill="none" stroke="#ffffff" stroke-width="3">
      <rect x="1.5" y="1.5" width="38" height="28"/>
      <circle cx="11" cy="10" r="3.5" fill="#ffffff" stroke="none"/>
      <polyline points="5,26 15,16 21,22 28,12 36,26" fill="#ffffff" stroke="none"/>
    </g>
    <text class="member-name orange" x="811" y="242">MARCUS R. DELANE</text>
    <text class="member-role" x="811" y="262">Chief Innovator Officer</text>
    <text class="member-bio" x="811" y="300">Early Ledgerline employee</text>
    <text class="member-bio" x="811" y="315.5">Formed LL Advisors</text>
    <text class="member-bio" x="811" y="331">Launched passively managed</text>
    <text class="member-bio" x="811" y="346.5">index funds</text>
  </g>

  <g class="member member-tech">
    <polygon points="122,409 582,409 351,624" fill="var(--teal)"/>
    <circle cx="444" cy="517" r="75" fill="var(--placeholder)" role="img" aria-label="Portrait of Henrik Voss"/>
    <g class="photo-icon" transform="translate(424,499)" fill="none" stroke="#ffffff" stroke-width="3">
      <rect x="1.5" y="1.5" width="38" height="28"/>
      <circle cx="11" cy="10" r="3.5" fill="#ffffff" stroke="none"/>
      <polyline points="5,26 15,16 21,22 28,12 36,26" fill="#ffffff" stroke="none"/>
    </g>
    <text class="member-name teal" x="558" y="455">HENRIK VOSS</text>
    <text class="member-role" x="558" y="475">Chief Technology Officer</text>
    <text class="member-bio" x="558" y="513">Over 13 years of programming experience</text>
    <text class="member-bio" x="558" y="528.5">Graduate of Westbrook University</text>
  </g>

  <g class="page-tag">
    <polygon points="1074,631 1200,645 1200,708 1113,722" fill="var(--blue)"/>
    <text class="page-label" x="1173" y="671" text-anchor="end">Page</text>
    <text class="page-number" x="1171" y="697" text-anchor="end">10</text>
  </g>
</svg>
</body>
</html>
```